Consulting/Brand Licensing business needs business card

We need a business card created for our IP company, that also does consulting and brand licensing. We would like this card to be vague, as our other business' are in the cannabis industry and this is a non-cannabis touching entity. Perhaps something that hints vaguely at the industry without alerting or possibly offending the receiver.

Target Market(s)

CEOs/Key Decision Makers/Industry Leaders

Contact Information for Business Card

No address, simply list Seattle, WA. Phone: 206-555-0147. Name: Dilan Vesterby // email: Dilan@pulvanixa.com

Colors

Designer to choose colors to be used in the design.

Requirements
Must have
• Logo, Name, Email, Phone number, "Consulting, Licensing and Branding Specialists"
Nice to have
• We would like this to be more professional than playful.

```html
<!DOCTYPE html>
<html lang="en">
<head>
<meta charset="utf-8">
<title>Pulvanixa, Inc — Business Card</title>
<link href="https://fonts.googleapis.com/css2?family=Montserrat:wght@700&family=Questrial&family=Roboto:wght@400;700&display=swap" rel="stylesheet">
<style>
  :root {
    --backdrop: #2f2824;
    --card: #1d1f21;
    --card-edge: #141516;
    --accent: #e2492b;
    --accent-muted: #a9432f;
    --text-light: #f1f1f1;
    --text-soft: #b9b9b9;
    --rule: #5a5c5e;
  }
  * { margin: 0; padding: 0; box-sizing: border-box; }
  html, body {
    width: 1200px; height: 769px; overflow: hidden;
    background: var(--backdrop);
  }
  .canvas {
    position: relative; width: 1200px; height: 769px;
    display: flex; align-items: center; justify-content: center; gap: 50px;
  }
  .card {
    position: relative; width: 530px; height: 303px;
    background: var(--card);
    border-radius: 3px;
    box-shadow: 0 18px 40px rgba(0,0,0,.45), 0 0 0 1px var(--card-edge);
  }
  /* Front */
  .card--front {
    display: flex; flex-direction: column; align-items: center; justify-content: center;
  }
  .wordmark {
    font-family: "Montserrat", sans-serif; font-weight: 700;
    font-size: 54px; letter-spacing: 1px; line-height: 1;
    color: var(--accent);
    white-space: nowrap;
  }
  .card--front .wordmark { color: var(--accent-muted); }
  .company-name {
    font-family: "Questrial", sans-serif;
    font-size: 21px; color: var(--text-soft);
    margin-top: 8px; letter-spacing: .3px;
  }
  .tagline {
    font-family: "Questrial", sans-serif;
    font-size: 12px; letter-spacing: 1px; color: var(--text-soft);
    margin-top: 10px;
  }
  .web-spaced {
    font-family: "Questrial", sans-serif;
    font-size: 13px; letter-spacing: 6px; color: var(--text-soft);
    margin-top: 26px;
  }
  /* Back */
  .card--back { display: flex; align-items: center; }
  .brand-block {
    width: 270px; padding-left: 34px; padding-right: 20px;
    display: flex; flex-direction: column; align-items: flex-start;
  }
  .card--back .wordmark { font-size: 32px; letter-spacing: .5px; }
  .card--back .company-name { font-size: 17px; color: var(--text-light); }
  .divider {
    width: 1px; height: 130px; background: var(--rule); flex: none;
  }
  .contact-block { padding-left: 24px; font-family: "Roboto", sans-serif; }
  .person-name {
    font-weight: 700; font-size: 19px; color: var(--accent);
    text-transform: uppercase; letter-spacing: .2px; white-space: nowrap;
  }
  .location { font-size: 14px; color: var(--text-light); margin: 6px 0 10px; }
  .contact-list { list-style: none; }
  .contact-list li {
    display: flex; align-items: center; gap: 7px;
    font-size: 14px; color: var(--text-light); line-height: 1.45; white-space: nowrap;
  }
  .contact-list svg { width: 11px; height: 11px; fill: var(--accent); flex: none; }
</style>
</head>
<body>
<main class="canvas">
  <section class="card card--front" aria-label="Card front">
    <div class="wordmark">PULVANIXA</div>
    <div class="company-name">Pulvanixa, Inc</div>
    <div class="tagline">Consulting, Licensing and Branding Specialists</div>
    <div class="web-spaced">www.pulvanixa.com</div>
  </section>

  <section class="card card--back" aria-label="Card back">
    <div class="brand-block">
      <div class="wordmark">PULVANIXA</div>
      <div class="company-name">Pulvanixa, Inc</div>
    </div>
    <div class="divider"></div>
    <div class="contact-block">
      <div class="person-name">Dilan Vesterby</div>
      <div class="location">Seattle, WA.</div>
      <ul class="contact-list">
        <li>
          <svg viewBox="0 0 24 24" aria-hidden="true"><path d="M6.6 10.8a15 15 0 0 0 6.6 6.6l2.2-2.2a1 1 0 0 1 1-.25 11.4 11.4 0 0 0 3.6.57 1 1 0 0 1 1 1V20a1 1 0 0 1-1 1A17 17 0 0 1 3 4a1 1 0 0 1 1-1h3.5a1 1 0 0 1 1 1c0 1.25.2 2.45.57 3.57a1 1 0 0 1-.25 1z"/></svg>
          206-555-0147
        </li>
        <li>
          <svg viewBox="0 0 24 24" aria-hidden="true"><path d="M2 5h20v14H2z M2 5l10 8 10-8" stroke="#1d1f21" stroke-width="1.5"/></svg>
          Dilan@pulvanixa.com
        </li>
        <li>
          <svg viewBox="0 0 24 24" aria-hidden="true"><circle cx="12" cy="12" r="10"/><path d="M2 12h20M12 2c3 3 3 17 0 20M12 2c-3 3-3 17 0 20" stroke="#1d1f21" stroke-width="1.5" fill="none"/></svg>
          www.pulvanixa.com
        </li>
      </ul>
    </div>
  </section>
</main>
</body>
</html>
```